Real Estate "Top 10" Page design.

Design a page template for Wordpress website to feature an easily editable "top 10 real estate listings".

The design should be clean and easy on the eye but also needs to look impressive. Maybe the properties should magnify as you scroll over them? Use you design talents to create something cool but not tacky. It should in some way use the color scheme of my logo and the fonts. I must be able to move the listings to different positions easily and I want to be able to add properties to the template from the individual IDX listings and link back from it to the individual listing page. I use a plug in for IDX from Brambleton solutions. [url removed, login to view]

I will provide the logins for my website to the winner.

As a guide the page currently can be found at:

Thanks in advance for your time.

```html
<!DOCTYPE html>
<html lang="en">
<head>
<meta charset="utf-8">
<title>Bozeman Real Estate – Top Listings</title>
<link rel="stylesheet" href="https://fonts.googleapis.com/css2?family=PT+Sans+Narrow:wght@400;700&family=Source+Sans+3:wght@400;600&display=swap">
<style>
  :root {
    --page: #ffffff;
    --card: #e6e6e6;
    --ink: #2b2b2b;
    --accent: #e8734f;
    --status: #e0342b;
    --brand: #d9774f;
  }
  * { box-sizing: border-box; margin: 0; padding: 0; }
  html, body { width: 770px; height: 1200px; overflow: hidden; background: var(--page); }
  body { position: relative; font-family: "Source Sans 3", sans-serif; color: var(--ink); }

  .listing {
    position: absolute;
    left: 0;
    width: 770px;
    background: var(--card);
  }
  .listing--first  { top: 19px;  height: 357px; }
  .listing--second { top: 409px; height: 376px; }
  .listing--third  { top: 823px; height: 377px; }

  .listing__photo {
    position: absolute;
    left: 15px;
    width: 516px;
  }
  .listing--first  .listing__photo { top: 7px;  height: 329px; background: linear-gradient(160deg, #5b6a80 0%, #8c7e6c 55%, #5e8ea3 100%); }
  .listing--second .listing__photo { top: 20px; height: 339px; background: linear-gradient(170deg, #4869a0 0%, #9aa0a8 55%, #4f6b42 100%); }
  .listing--third  .listing__photo { top: 24px; height: 332px; background: linear-gradient(165deg, #8a7f98 0%, #6a6670 50%, #4f4f4e 100%); }

  .brand {
    position: absolute;
    top: 12px;
    right: 14px;
    display: flex;
    align-items: center;
    gap: 6px;
    font-family: "PT Sans Narrow", sans-serif;
    font-size: 15px;
    font-weight: 400;
    letter-spacing: 0.5px;
    color: var(--brand);
  }
  .brand__mark { width: 9px; height: 9px; background: var(--brand); }

  .listing__tag {
    position: absolute;
    left: 132px;
    top: 255px;
    width: 253px;
    height: 34px;
    background: #f4f4f4;
    font-family: "PT Sans Narrow", sans-serif;
    font-weight: 700;
    font-size: 17px;
    line-height: 34px;
    padding-left: 34px;
    color: var(--ink);
  }

  .listing__info {
    position: absolute;
    left: 548px;
    width: 208px;
  }
  .listing--first  .listing__info { top: 6px; }
  .listing--second .listing__info { top: 20px; }
  .listing--third  .listing__info { top: 22px; }

  .listing__title {
    font-family: "PT Sans Narrow", sans-serif;
    font-weight: 700;
    font-size: 21px;
    letter-spacing: 0.2px;
    line-height: 26px;
    margin-bottom: 2px;
  }
  .facts { list-style: none; }
  .facts li {
    display: flex;
    font-family: "PT Sans Narrow", sans-serif;
    font-size: 20px;
    line-height: 26px;
  }
  .facts__label { width: 61px; }
  .facts__sep { width: 12px; }
  .facts__value { color: var(--accent); font-weight: 700; }
  .facts__value--status { color: var(--status); }

  .listing__desc {
    margin-top: 5px;
    font-size: 10.2px;
    line-height: 12.7px;
    text-align: justify;
  }
</style>
</head>
<body>

<article class="listing listing--first">
  <div class="listing__photo" role="img" aria-label="Modern home at dusk with lit covered patio, lounge chairs, hot tub and pool">
    <div class="brand"><span class="brand__mark"></span>HAL BRENNER MONTANA</div>
  </div>
  <div class="listing__info">
    <h2 class="listing__title">BOZEMAN REAL ESTATE</h2>
    <ul class="facts">
      <li><span class="facts__label">Street</span><span class="facts__sep">:</span><span class="facts__value">412 W Alder</span></li>
      <li><span class="facts__label">Price</span><span class="facts__sep">:</span><span class="facts__value">$995,000</span></li>
      <li><span class="facts__label">Beds</span><span class="facts__sep">:</span><span class="facts__value">7 Pc’s</span></li>
      <li><span class="facts__label">Baths</span><span class="facts__sep">:</span><span class="facts__value">7 Pc’s</span></li>
      <li><span class="facts__label">Size</span><span class="facts__sep">:</span><span class="facts__value">5,822 sq ft</span></li>
      <li><span class="facts__label">Status</span><span class="facts__sep">:</span><span class="facts__value facts__value--status">Active</span></li>
    </ul>
    <p class="listing__desc">3 separate living quarters – the Main House, a Basement Apartment w/private entrance and 9 foot ceilings, and a Studio Apartment in the Carriage House offer a variety of living and investment possibilities. Unique property convenient to historic downtown Bozeman, near campus and Aspen Park. Buyer to verify square footage. The Thornbury House was built in the 1890’s by Bozeman Pioneer Elias Thornbury. The Carriage House was added in 2004. Listing provided by Mara Linden, Ridgeline Realty – Downtown</p>
  </div>
</article>

<article class="listing listing--second">
  <div class="listing__photo" role="img" aria-label="White curved-facade villa at dusk with palm trees and lit lawn">
    <div class="brand"><span class="brand__mark"></span>HAL BRENNER MONTANA</div>
  </div>
  <div class="listing__info">
    <h2 class="listing__title">BOZEMAN REAL ESTATE</h2>
    <ul class="facts">
      <li><span class="facts__label">Street</span><span class="facts__sep">:</span><span class="facts__value">412 W Alder</span></li>
      <li><span class="facts__label">Price</span><span class="facts__sep">:</span><span class="facts__value">$995,000</span></li>
      <li><span class="facts__label">Beds</span><span class="facts__sep">:</span><span class="facts__value">7 Pc’s</span></li>
      <li><span class="facts__label">Baths</span><span class="facts__sep">:</span><span class="facts__value">7 Pc’s</span></li>
      <li><span class="facts__label">Size</span><span class="facts__sep">:</span><span class="facts__value">5,822 sq ft</span></li>
      <li><span class="facts__label">Status</span><span class="facts__sep">:</span><span class="facts__value facts__value--status">Active</span></li>
    </ul>
    <p class="listing__desc">3 separate living quarters – the Main House, a Basement Apartment w/private entrance and 9 foot ceilings, and a Studio Apartment in the Carriage House offer a variety of living and investment possibilities. Unique property convenient to historic downtown Bozeman, near campus and Aspen Park. Buyer to verify square footage. The Thornbury House was built in the 1890’s by Bozeman Pioneer Elias Thornbury. The Carriage House was added in 2004. Listing provided by Mara Linden, Ridgeline Realty – Downtown</p>
  </div>
</article>

<article class="listing listing--third">
  <div class="listing__photo" role="img" aria-label="White clapboard house at twilight with lit porch, bare trees and a tall evergreen">
    <div class="brand"><span class="brand__mark"></span>HAL BRENNER MONTANA</div>
    <div class="listing__tag">delete</div>
  </div>
  <div class="listing__info">
    <h2 class="listing__title">BOZEMAN REAL ESTATE</h2>
    <ul class="facts">
      <li><span class="facts__label">Street</span><span class="facts__sep">:</span><span class="facts__value">412 W Alder</span></li>
      <li><span class="facts__label">Price</span><span class="facts__sep">:</span><span class="facts__value">$995,000</span></li>
      <li><span class="facts__label">Beds</span><span class="facts__sep">:</span><span class="facts__value">7 Pc’s</span></li>
      <li><span class="facts__label">Baths</span><span class="facts__sep">:</span><span class="facts__value">7 Pc’s</span></li>
      <li><span class="facts__label">Size</span><span class="facts__sep">:</span><span class="facts__value">5,822 sq ft</span></li>
      <li><span class="facts__label">Status</span><span class="facts__sep">:</span><span class="facts__value facts__value--status">Active</span></li>
    </ul>
    <p class="listing__desc">3 separate living quarters – the Main House, a Basement Apartment w/private entrance and 9 foot ceilings, and a Studio Apartment in the Carriage House offer a variety of living and investment possibilities. Unique property convenient to historic downtown Bozeman, near campus and Aspen Park. Buyer to verify square footage. The Thornbury House was built in the 1890’s by Bozeman Pioneer Elias Thornbury. The Carriage House was added in 2004. Listing provided by Mara Linden, Ridgeline Realty – Downtown</p>
  </div>
</article>

</body>
</html>
```